Waste Oil Filter collection & disposal

Basically I need a 1 page website for the business called Brenmoor Waste Solutions.
We are a environmental service provider and we collect and dispose of waste oil filters to protect the environment from hazardous waste oil products.

This is the link to our current website: www.brenmoorwaste.co.nz

we want it to look fresh and better than our current website. we may potentially look at getting a new logo designed and are open to ideas/designs if you have any.

Industry/Entity Type

Business

Logo Text

Brenmoor Waste Solutions

Number of Pages Required

1 page

Requirements
Must have
• same colours as current website.
• description of what service we provide please refer to leaflet attached

```html
<!DOCTYPE html>
<html lang="en">
<head>
<meta charset="utf-8">
<title>Brenmoor Waste Solutions</title>
<link href="https://fonts.googleapis.com/css2?family=Oswald:wght@500;600&family=Montserrat:wght@400;500;600;700;800&display=swap" rel="stylesheet">
<style>
:root{
  --green:#4fa62b;
  --green-dark:#3b8a1f;
  --green-pale:#c9e8b4;
  --ink:#222222;
  --text:#444444;
  --muted:#777777;
  --white:#ffffff;
  --footer:#1d1d1d;
  --hero-top:#5f6a62;
  --hero-bottom:#2c3a30;
}
*{box-sizing:border-box;margin:0;padding:0}
html,body{width:1200px;height:3147px;overflow:hidden}
body{position:relative;background:var(--white);font-family:"Montserrat",sans-serif;color:var(--text)}
.abs{position:absolute}

/* header */
.site-header{left:0;top:0;width:1200px;height:95px;background:var(--white)}
.brand{left:85px;top:24px;display:flex;align-items:center;gap:10px}
.brand-mark{width:40px;height:40px;border-radius:50%;background:var(--green)}
.brand-name{font-weight:700;font-size:17px;color:var(--ink);line-height:1.15;width:190px}
.main-nav{left:390px;top:38px;display:flex;gap:36px;font-size:16px;color:#555}
.header-contact{right:87px;top:22px;text-align:right;font-size:15px;color:#444;line-height:30px}
.header-contact svg{vertical-align:-2px;margin-right:6px}

/* hero */
.hero{left:0;top:95px;width:1200px;height:551px;background:linear-gradient(160deg,var(--hero-top),var(--hero-bottom))}
.hero-title{left:0;top:280px;width:1200px;text-align:center;font-family:"Oswald",sans-serif;font-weight:600;font-size:56px;line-height:64px;color:var(--white);letter-spacing:1px}
.hero-sub{left:0;top:346px;width:1200px;text-align:center;font-family:"Oswald",sans-serif;font-weight:500;font-size:28px;line-height:34px;color:var(--white);letter-spacing:1px}
.hero-text{left:170px;top:396px;width:860px;text-align:center;font-size:16px;line-height:26px;color:var(--white)}
.scroll-cue{left:584px;top:525px}

/* service cards */
.service-card{top:648px;width:323px;height:197px;background:var(--green);color:var(--white);text-align:center;border:1px solid rgba(255,255,255,.35);outline:3px solid var(--green);outline-offset:-10px;overflow:hidden}
.service-card h3{font-weight:500;font-size:25px;line-height:32px;margin-top:36px;white-space:nowrap;padding:0 12px}
.service-card h3.long{font-size:20px}
.service-card .rule{width:38px;height:3px;background:var(--white);margin:12px auto 12px}
.service-card p{font-size:13.5px;line-height:22px;padding:0 55px}

/* welcome */
.welcome{left:0;top:918px;width:1200px;text-align:center}
.welcome .kicker{font-size:24px;color:var(--ink)}
.welcome h2{font-size:29px;font-weight:700;color:var(--ink);margin-top:4px}
.recycle-icon{display:block;margin:8px auto 0}
.welcome .lead{font-size:15px;color:var(--text);margin-top:20px}
.welcome .body{font-size:13.5px;line-height:26px;color:var(--text);width:980px;margin:10px auto 0}

/* process */
.process{left:0;top:1178px;width:1200px;height:402px;background:var(--green-pale)}
.section-title{width:1200px;left:0;text-align:center;font-size:30px;font-weight:800;color:var(--ink)}
.process-sub{left:0;top:1296px;width:1200px;text-align:center;font-size:15px;color:var(--ink)}
.step{top:1350px;width:180px;text-align:center}
.step-ring{width:118px;height:118px;margin:0 auto;border-radius:50%;border:6px solid var(--green);display:flex;align-items:center;justify-content:center;background:var(--green-pale)}
.step-core{width:88px;height:88px;border-radius:50%;background:var(--white);border:4px solid var(--ink);display:flex;align-items:center;justify-content:center}
.step-label{margin-top:24px;font-size:17px;line-height:22px;color:var(--ink)}

/* split */
.plant-photo{left:0;top:1580px;width:588px;height:420px;background:linear-gradient(135deg,#8d9690,#2f6b45 55%,#1f3a2a)}
.about{left:612px;top:1640px;width:500px}
.about h3{font-size:18px;font-weight:500;line-height:28px;color:var(--ink);margin-bottom:18px}
.about p{font-size:13.5px;line-height:24px;color:var(--text);margin-bottom:16px}
.about hr{border:0;border-top:1px solid #ddd;margin:-2px 0 16px}

/* gallery */
.gallery-item{background:linear-gradient(150deg,#55605a,#1f3327)}
.arrow{top:2352px}

/* map & footer */
.map{left:0;top:2690px;width:1200px;height:400px;background:linear-gradient(120deg,#eeeeec,#e2e6e4 50%,#7cc8ec 70%,#ececea)}
.site-footer{left:0;top:3090px;width:1200px;height:57px;background:var(--footer)}
.site-footer .copy{left:85px;top:20px;font-size:13px;color:#9a9a9a}
.social{top:20px;width:16px;height:16px;border-radius:50%;background:var(--green)}
</style>
</head>
<body>

<header class="site-header abs">
  <div class="brand abs"><span class="brand-mark"></span><span class="brand-name">Brenmoor Waste Solutions</span></div>
  <nav class="main-nav abs"><span>Home</span><span>About Us</span><span>Recycle</span><span>Gallery</span><span>Contact Us</span></nav>
  <div class="header-contact abs">
    <div><svg width="13" height="13" viewBox="0 0 24 24"><path fill="#444" d="M6.6 10.8a15 15 0 0 0 6.6 6.6l2.2-2.2c.3-.3.7-.4 1-.2 1.1.4 2.3.6 3.6.6.6 0 1 .4 1 1V20c0 .6-.4 1-1 1A17 17 0 0 1 3 4c0-.6.4-1 1-1h3.5c.6 0 1 .4 1 1 0 1.3.2 2.5.6 3.6.1.3 0 .7-.2 1z"/></svg>06 555 0148</div>
    <div><svg width="14" height="12" viewBox="0 0 24 18"><rect x="1" y="1" width="22" height="16" rx="2" fill="#444"/><path d="M2 2l10 8 10-8" stroke="#fff" stroke-width="2" fill="none"/></svg>info@brenmoorwaste.co.nz</div>
  </div>
</header>

<section class="hero abs" role="img" aria-label="Photo of a green and grey waste collection truck parked on grass"></section>
<h1 class="hero-title abs">BRENMOOR WASTE SOLUTIONS</h1>
<div class="hero-sub abs">KEEPING NEWZEALAND GREEN</div>
<p class="hero-text abs">We offer a cost effective environmentally friendly system for the collection and disposal of waste oil filters helping minimise contamination of landfills keeping your industry compliant.</p>
<svg class="scroll-cue abs" width="32" height="66" viewBox="0 0 32 66"><rect x="8" y="1" width="16" height="28" rx="8" fill="none" stroke="#fff" stroke-width="2"/><line x1="16" y1="8" x2="16" y2="14" stroke="#fff" stroke-width="2"/><path d="M7 38l9 8 9-8M7 48l9 8 9-8" fill="none" stroke="#fff" stroke-width="2"/></svg>

<div class="service-card abs" style="left:85px"><h3>GreenLoop Trust</h3><div class="rule"></div><p>each used oil filter has on aver age, more than quar ter of a litre of used motor oil</p></div>
<div class="service-card abs" style="left:439px"><h3>Oil Recycling</h3><div class="rule"></div><p>each used oil filter has on aver age, more than quar ter of a litre of used motor oil</p></div>
<div class="service-card abs" style="left:790px"><h3 class="long">Harbourside District Council</h3><div class="rule"></div><p>each used oil filter has on aver age, more than quar ter of a litre of used motor oil</p></div>

<section class="welcome abs">
  <div class="kicker">Welcome to</div>
  <h2>Brenmoor Waste Solutions Ltd</h2>
  <svg class="recycle-icon" width="26" height="24" viewBox="0 0 26 24"><path d="M13 2l5 8h-4l-1-1.6L9 14H5z M22 14l3 6H15l2-3h3z M3 20l-2-4 4-6 2 3-2 3h6v4z" fill="var(--green)"/></svg>
  <p class="lead">Brenmoor Waste Solutions Ltd specialize in the collection &amp; disposal of oil / fuel filters, servicing the lower north island on a monthly cycle.</p>
  <p class="body">Lorem Ipsum is simply dummy text of the printing and typesetting industry. Lorem Ipsum has been the industry's standard dummy text ever since the 1500s, when an unknown printer took a galley of type</p>
</section>

<section class="process abs"></section>
<h2 class="section-title abs" style="top:1212px">THE PROCESS</h2>
<svg class="abs" style="left:587px;top:1256px" width="26" height="24" viewBox="0 0 26 24"><path d="M13 2l5 8h-4l-1-1.6L9 14H5z M22 14l3 6H15l2-3h3z M3 20l-2-4 4-6 2 3-2 3h6v4z" fill="var(--green)"/></svg>
<p class="process-sub abs">Filters are collected and transported back to the processing plant.</p>

<div class="step abs" style="left:70px"><div class="step-ring"><div class="step-core"><svg width="40" height="44" viewBox="0 0 40 44"><rect x="6" y="8" width="28" height="34" rx="2" fill="none" stroke="#222" stroke-width="3"/><line x1="2" y1="6" x2="38" y2="6" stroke="#222" stroke-width="3"/><path d="M14 14v22M20 14v22M26 14v22" stroke="#222" stroke-width="2.5"/></svg></div></div><div class="step-label">Drained</div></div>
<div class="step abs" style="left:245px"><div class="step-ring"><div class="step-core"><svg width="40" height="40" viewBox="0 0 40 40"><rect x="6" y="4" width="28" height="22" fill="#222"/><path d="M8 28v10M13 28v10M18 28v10M23 28v10M28 28v10M33 28v10" stroke="#222" stroke-width="2.5"/></svg></div></div><div class="step-label">Sorted</div></div>
<div class="step abs" style="left:420px"><div class="step-ring"><div class="step-core"><svg width="44" height="40" viewBox="0 0 44 40"><rect x="3" y="3" width="38" height="34" rx="5" fill="none" stroke="#222" stroke-width="3"/><path d="M12 16h18l-4-4M32 24H14l4 4" fill="none" stroke="var(--green)" stroke-width="3"/></svg></div></div><div class="step-label">Drained again</div></div>
<div class="step abs" style="left:600px"><div class="step-ring"><div class="step-core"><svg width="44" height="40" viewBox="0 0 44 40"><rect x="14" y="4" width="16" height="14" fill="none" stroke="#222" stroke-width="2.5"/><rect x="4" y="22" width="16" height="14" fill="none" stroke="#222" stroke-width="2.5"/><rect x="24" y="22" width="16" height="14" fill="none" stroke="#222" stroke-width="2.5"/></svg></div></div><div class="step-label">Crushed into<br>bricks</div></div>
<div class="step abs" style="left:775px"><div class="step-ring"><div class="step-core"><svg width="36" height="42" viewBox="0 0 36 42"><path d="M4 3h28M4 39h28M8 3c0 12 20 12 20 18S8 27 8 39M28 3c0 12-20 12-20 18s20 6 20 18" fill="none" stroke="#222" stroke-width="3"/><path d="M12 34h12l-6-6z" fill="var(--green)"/></svg></div></div><div class="step-label">Drained a third<br>time</div></div>
<div class="step abs" style="left:950px"><div class="step-ring"><div class="step-core"><svg width="40" height="42" viewBox="0 0 40 42"><rect x="6" y="4" width="26" height="34" rx="3" fill="none" stroke="#222" stroke-width="3" transform="rotate(-8 20 21)"/><path d="M20 14l5 8h-4M16 26h10" fill="none" stroke="var(--green)" stroke-width="2.5"/></svg></div></div><div class="step-label">Stacked ready for<br>Metal Recycling</div></div>

<div class="plant-photo abs" role="img" aria-label="Photo of a green filter crushing machine inside the processing plant"></div>
<section class="about abs">
  <h3>Brenmoor Waste Solutions Ltd service the Lower North Island and</h3>
  <p>We are passionate about doing our bit in keeping New Zealand Clean and Green.</p>
  <p>We offer a cost effective system for the collection and disposal of waste oil filters.</p>
  <hr>
  <p>Our processes are environmentally friendly and minimise the contamination of landfills.</p>
  <p>We keep your industry compliant.</p>
</section>

<h2 class="section-title abs" style="top:2060px">OUR GALLERY</h2>
<svg class="abs" style="left:587px;top:2102px" width="26" height="24" viewBox="0 0 26 24"><path d="M13 2l5 8h-4l-1-1.6L9 14H5z M22 14l3 6H15l2-3h3z M3 20l-2-4 4-6 2 3-2 3h6v4z" fill="var(--green)"/></svg>
<div class="gallery-item abs" style="left:85px;top:2150px;width:325px;height:385px" role="img" aria-label="Photo of a worker operating machinery in the plant"></div>
<svg class="abs" style="left:225px;top:2322px" width="44" height="44" viewBox="0 0 44 44"><path d="M26 4h14v14M40 4L26 18M18 40H4V26M4 40l14-14" fill="none" stroke="#fff" stroke-width="2.5"/></svg>
<div class="gallery-item abs" style="left:437px;top:2150px;width:325px;height:182px;background:linear-gradient(150deg,#9aa0a6,#40444a)" role="img" aria-label="Photo of a pile of used oil filters"></div>
<div class="gallery-item abs" style="left:437px;top:2352px;width:325px;height:183px;background:linear-gradient(150deg,#b8bcc0,#3f6a4e)" role="img" aria-label="Photo of crushed filter bricks on plant benches"></div>
<div class="gallery-item abs" style="left:790px;top:2150px;width:323px;height:385px;background:linear-gradient(150deg,#a6aaa8,#2f6b45 60%,#1e3a29)" role="img" aria-label="Photo of the green filter crushing machine"></div>
<svg class="arrow abs" style="left:36px" width="34" height="34" viewBox="0 0 34 34"><path d="M20 6L8 17l12 11M8 17h22" fill="none" stroke="var(--green)" stroke-width="4"/></svg>
<svg class="arrow abs" style="left:1130px" width="34" height="34" viewBox="0 0 34 34"><path d="M14 6l12 11-12 11M26 17H4" fill="none" stroke="var(--green)" stroke-width="4"/></svg>

<h2 class="section-title abs" style="top:2592px">FIND US</h2>
<svg class="abs" style="left:587px;top:2634px" width="26" height="24" viewBox="0 0 26 24"><path d="M13 2l5 8h-4l-1-1.6L9 14H5z M22 14l3 6H15l2-3h3z M3 20l-2-4 4-6 2 3-2 3h6v4z" fill="var(--green)"/></svg>
<div class="map abs" role="img" aria-label="Map showing the business location"></div>

<footer class="site-footer abs">
  <div class="copy abs">© 2017 / All Rights Reserved</div>
  <span class="social abs" style="left:1064px"></span>
  <span class="social abs" style="left:1092px"></span>
</footer>

</body>
</html>
```